Re-design Company presentation for FenLoopVault

The current presentation has the right content, but we need to make serious changes in terms of colors, backgrounds, etc.
You can view the current state of the PPT as a skeleton that needs to be revamped to make it look professional & visually appealing.
Please feel free to make any changes as necessary, but please maintain text editable and consider that we might add for example new individual client logos in the future, so generally avoid large chunks of images combined together.
If you require any specific logos in a better format, or if you have any questions at all, please feel free to ask.

```html
<!DOCTYPE html>
<html lang="en">
<head>
<meta charset="utf-8">
<title>FenLoopVault – Company Presentation</title>
<link href="https://fonts.googleapis.com/css2?family=Montserrat:ital,wght@0,400;0,500;0,600;0,700;0,800;1,600&display=swap" rel="stylesheet">
<style>
:root{
  --stage:#9e9e9e;
  --navy:#0b1535;
  --navy-deep:#050a1f;
  --ink:#1d1d1f;
  --body:#333;
  --pink:#c8337d;
  --pink-deep:#a8246a;
  --purple:#6b3b78;
  --teal:#1f5f78;
  --track:#e0e0e0;
  --cell-line:#e4e4e4;
  --white:#fff;
}
*{margin:0;padding:0;box-sizing:border-box}
html,body{width:1200px;height:3859px;overflow:hidden}
body{background:var(--stage);font-family:"Montserrat",sans-serif;color:var(--body);position:relative}
.slide{position:absolute;left:81px;width:1038px;height:585px;background:var(--white);overflow:hidden}
.slide--cover{top:70px}
.slide--vision{top:694px}
.slide--services{top:1317px}
.slide--problems{top:1940px}
.slide--cms{top:2563px}
.slide--thanks{top:3186px}
.abs{position:absolute}
.tab{position:absolute;left:0;top:22px;height:36px;padding:0 28px 0 34px;border-radius:0 18px 18px 0;background:linear-gradient(90deg,var(--pink-deep),var(--pink));color:var(--white);font-size:11px;font-weight:700;line-height:36px;letter-spacing:.2px}
.heading{font-size:26px;font-weight:800;color:var(--ink);letter-spacing:.3px}
.heading--center{position:absolute;left:0;right:0;text-align:center}

/* cover */
.cover-bg{position:absolute;inset:0;background:radial-gradient(ellipse at 60% 40%,#1c2c66 0%,#0e1a45 45%,var(--navy-deep) 100%)}
.cover-title{left:54px;top:118px;font-size:47px;font-weight:800;line-height:57px;color:var(--white)}
.brand{display:flex;align-items:center;gap:14px;color:var(--white);font-weight:500}
.brand__box{width:26px;height:26px;background:var(--white)}
.cover-brand{left:54px;top:460px;font-size:32px}
.cover-tagline{left:744px;top:398px;font-size:23px;font-weight:700;line-height:29px;color:var(--white)}
.cover-meta{left:744px;top:468px;font-size:12.5px;line-height:19px;color:#d8dbe8}

/* vision */
.vision-title{left:45px;top:136px}
.vision-copy{left:45px;top:183px;width:394px;font-size:12.5px;line-height:19.5px;color:var(--body)}
.vision-copy p{margin-bottom:19.5px;text-align:justify}
.quote{left:574px;top:360px;font-size:16px;font-style:italic;font-weight:600;line-height:18px;color:var(--white)}
.quote-author{right:92px;top:324px;text-align:right;font-size:13px;font-style:italic;font-weight:600;line-height:16px;color:var(--white)}
.signature{left:750px;top:365px;width:150px;height:20px;background:rgba(255,255,255,.25);border-radius:10px}

/* services */
.services-title{top:56px}
.service h3{font-size:15.5px;font-weight:700;line-height:20px;color:var(--ink);margin-bottom:8px}
.service p{font-size:10.8px;line-height:15.6px;color:var(--body)}
.service--right{text-align:right}
.svc-analytics{left:95px;top:168px;width:230px}
.svc-strategy{left:80px;top:376px;width:283px}
.svc-advanced{left:690px;top:100px;width:222px}
.svc-continuous{left:711px;top:334px;width:226px}

/* problems */
.problems-title{top:90px}
.problems-sub{position:absolute;left:0;right:0;top:140px;text-align:center;font-size:17px;line-height:24px;color:var(--ink)}
.stat{position:absolute;top:228px;width:260px;text-align:center}
.stat__ring{position:relative;width:168px;height:168px;margin:0 auto}
.stat__value{position:absolute;inset:0;display:flex;align-items:center;justify-content:center;font-size:46px;font-weight:800;color:var(--ink);letter-spacing:-1px}
.stat__value small{font-size:22px;font-weight:700;margin-top:12px;letter-spacing:0}
.stat__label{margin-top:18px;font-size:16.5px;line-height:19.5px;color:var(--body)}

/* cms */
.cms-title{top:58px}
.cms-grid{position:absolute;left:138px;top:132px;display:grid;grid-template-columns:repeat(4,182px);grid-auto-rows:90px;gap:9px 11px}
.cms-cell{border:1px solid var(--cell-line);display:flex;align-items:center;justify-content:center;gap:9px;font-size:20px;font-weight:600}
.cms-dot{width:22px;height:22px;border-radius:50%}

/* thanks */
.thanks-bg{position:absolute;inset:0;background:radial-gradient(ellipse at 30% 80%,#17295e 0%,#0b1535 50%,#03061a 100%)}
.thanks-title{position:absolute;left:0;right:0;top:60px;text-align:center;font-size:30px;font-weight:800;color:var(--white)}
.thanks-brand{left:100px;top:430px;font-size:56px}
.thanks-brand .brand__box{width:40px;height:40px}
.contact-title{left:620px;top:146px;font-size:32px;font-weight:800;line-height:44px;color:var(--white)}
.contact-row{position:absolute;left:620px;width:390px;display:flex;align-items:center;gap:18px;color:var(--white);font-size:15px;font-weight:500}
.contact-row__icon{width:44px;height:44px;border-radius:50%;background:var(--pink);display:flex;align-items:center;justify-content:center;flex:none}
.contact-rule{position:absolute;left:620px;width:390px;height:1px;background:rgba(255,255,255,.2)}
</style>
</head>
<body>

<!-- Cover -->
<section class="slide slide--cover">
  <div class="cover-bg" role="img" aria-label="Dark blue photograph of a data centre with a person working among server racks"></div>
  <h1 class="abs cover-title">FENLOOP<br>VAULT</h1>
  <div class="abs brand cover-brand"><span class="brand__box"></span>FenLoopVault</div>
  <h2 class="abs cover-tagline">Tagging Data You<br>Can Trust</h2>
  <p class="abs cover-meta">Proposal Created for {Company} by<br>Dara Volkov &amp; Owen Maddox {Date}</p>
</section>

<!-- Vision -->
<section class="slide slide--vision">
  <div class="tab">OUR VISION</div>
  <h2 class="abs heading vision-title">OUR VISION</h2>
  <div class="abs vision-copy">
    <p>We understand the importance of data-driven decisions in organisations of all sizes. If the data collected from your website / app is incorrect, or incomplete, then the outcome of your decisions is invariably a reflection of that.</p>
    <p>This is why our analytics implementation work is not only carefully vetted on multiple layers, but the implementation itself is engineered to include multiple fail-safes designed with data quality in mind.</p>
    <p>This is why our analytics implementation work is not only carefully vetted on multiple layers, but the implementation itself is engineered to include multiple fail-safes designed with data quality in mind.</p>
  </div>
  <svg class="abs" style="left:0;top:0" width="1038" height="585" viewBox="0 0 1038 585" aria-hidden="true">
    <defs>
      <linearGradient id="quoteLeft" x1="0" y1="0" x2="1" y2="1"><stop offset="0" stop-color="#d13a86"/><stop offset="1" stop-color="#b82a72"/></linearGradient>
      <linearGradient id="quoteRight" x1="0" y1="0" x2="1" y2="1"><stop offset="0" stop-color="#b5307a"/><stop offset="1" stop-color="#8e2363"/></linearGradient>
    </defs>
    <polygon points="837,191 987,341 837,491 687,341" fill="url(#quoteRight)"/>
    <polygon points="631,253 764,386 631,519 498,386" fill="url(#quoteLeft)"/>
  </svg>
  <p class="abs quote">In God we trust.<br>All others must<br>bring data.</p>
  <p class="abs quote-author">R. Halvorsen<br>Pike</p>
  <div class="abs signature" role="img" aria-label="Handwritten signature"></div>
</section>

<!-- Services -->
<section class="slide slide--services">
  <div class="tab">OUR SERVICES</div>
  <h2 class="heading heading--center services-title">OUR SERVICES</h2>
  <svg class="abs" style="left:0;top:0" width="1038" height="585" viewBox="0 0 1038 585" aria-hidden="true">
    <defs>
      <linearGradient id="svcRing" x1="0" y1="0" x2="1" y2="1"><stop offset="0" stop-color="#1f5f78"/><stop offset=".5" stop-color="#6b3b78"/><stop offset="1" stop-color="#c8337d"/></linearGradient>
    </defs>
    <circle cx="519" cy="295" r="118" fill="none" stroke="url(#svcRing)" stroke-width="22"/>
    <g fill="#0b1535" stroke="#fff" stroke-width="2">
      <circle cx="434" cy="207" r="39"/><circle cx="606" cy="205" r="39"/>
      <circle cx="441" cy="389" r="39"/><circle cx="606" cy="377" r="39"/>
    </g>
    <g fill="none" stroke="#fff" stroke-width="1.8" stroke-linecap="round" stroke-linejoin="round">
      <!-- dashboard board -->
      <rect x="416" y="193" width="36" height="24" rx="2"/><line x1="434" y1="217" x2="434" y2="224"/><line x1="426" y1="224" x2="442" y2="224"/>
      <polyline points="421,212 428,205 434,209 446,198"/>
      <!-- monitor with gear -->
      <rect x="588" y="191" width="36" height="24" rx="2"/><line x1="600" y1="222" x2="612" y2="222"/><line x1="606" y1="215" x2="606" y2="222"/>
      <circle cx="606" cy="203" r="5"/>
      <!-- bar chart -->
      <line x1="424" y1="405" x2="460" y2="405"/>
      <rect x="427" y="392" width="5" height="13"/><rect x="436" y="386" width="5" height="19"/><rect x="445" y="380" width="5" height="25"/>
      <polyline points="425,385 437,376 444,379 456,368"/><polyline points="451,368 456,368 456,373"/>
      <!-- shield -->
      <path d="M606 359 L622 365 L622 378 C622 388 615 394 606 398 C597 394 590 388 590 378 L590 365 Z"/>
      <polyline points="599,378 604,383 613,372"/>
    </g>
  </svg>
  <div class="abs service service--right svc-analytics">
    <h3>ANALYTICS<br>IMPLEMENTATION</h3>
    <p>We help you deploy analytics and measurement capabilities. Providing you with data and tagging expertise to create an effective reporting framework. We are specialists in data compliance, data privacy and consent management</p>
  </div>
  <div class="abs service service--right svc-strategy">
    <h3>DATA<br>STRATEGY</h3>
    <p>Starting from requirements gathering &amp; auditing your current set-up, to solution architecture &amp; continuous development plans, our team has the capability to take your project from its idea stages, to a fully-fledged business solution that can be used to expand your business.</p>
  </div>
  <div class="abs service svc-advanced">
    <h3>ADVANCED<br>TECHNOLOGIES</h3>
    <p>We partner with visionary customers who want to transform and grow their organization by building their business using modern digital marketing technologies. We develop custom data models to help you track revenue against marketing spend.</p>
  </div>
  <div class="abs service svc-continuous">
    <h3>CONTINUOUS<br>IMPROVEMENT</h3>
    <p>All our solutions are designed to include multiple fail-safes. Our code &amp; configurations are engineered to be robust and to allow future development. We include automated testing tools that can help our clients maintain high Data Quality standards at all times.</p>
  </div>
</section>

<!-- Problems -->
<section class="slide slide--problems">
  <div class="tab">DATA RELATED PROBLEMS</div>
  <h2 class="heading heading--center problems-title">DATA RELATED PROBLEMS</h2>
  <p class="problems-sub">Companies are struggling with data tagging, consent, privacy compliance<br>and the ability to measure return on marketing spend</p>
  <svg width="0" height="0" style="position:absolute" aria-hidden="true">
    <defs>
      <linearGradient id="statArc" x1="0" y1="0" x2="0" y2="1"><stop offset="0" stop-color="#1f5f78"/><stop offset=".5" stop-color="#6b3b78"/><stop offset="1" stop-color="#c8337d"/></linearGradient>
    </defs>
  </svg>
  <div class="stat" style="left:82px">
    <div class="stat__ring">
      <svg width="168" height="168" viewBox="0 0 168 168" aria-hidden="true">
        <circle cx="84" cy="84" r="72" fill="none" stroke="var(--track)" stroke-width="11"/>
        <circle cx="84" cy="84" r="72" fill="none" stroke="url(#statArc)" stroke-width="11" stroke-dasharray="384 452" transform="rotate(-90 84 84) scale(1 -1) translate(0 -168)"/>
      </svg>
      <div class="stat__value">85<small>%</small></div>
    </div>
    <p class="stat__label">of business are not fully confident in their consent management and privacy compliance strategy</p>
  </div>
  <div class="stat" style="left:377px">
    <div class="stat__ring">
      <svg width="168" height="168" viewBox="0 0 168 168" aria-hidden="true">
        <circle cx="84" cy="84" r="72" fill="none" stroke="var(--track)" stroke-width="11"/>
        <circle cx="84" cy="84" r="72" fill="none" stroke="url(#statArc)" stroke-width="11" stroke-dasharray="344 452" transform="rotate(-90 84 84) scale(1 -1) translate(0 -168)"/>
      </svg>
      <div class="stat__value">76<small>%</small></div>
    </div>
    <p class="stat__label">of businesses don't understand traffic sources or unable to visualize revenue against marketing sources</p>
  </div>
  <div class="stat" style="left:688px">
    <div class="stat__ring">
      <svg width="168" height="168" viewBox="0 0 168 168" aria-hidden="true">
        <circle cx="84" cy="84" r="72" fill="none" stroke="var(--track)" stroke-width="11"/>
        <circle cx="84" cy="84" r="72" fill="none" stroke="url(#statArc)" stroke-width="11" stroke-dasharray="334 452" transform="rotate(-90 84 84) scale(1 -1) translate(0 -168)"/>
      </svg>
      <div class="stat__value">74<small>%</small></div>
    </div>
    <p class="stat__label">of businesses don't have a universal data tagging governance in place</p>
  </div>
</section>

<!-- CMS -->
<section class="slide slide--cms">
  <div class="tab">CMS WE WORK WITH</div>
  <h2 class="heading heading--center cms-title">CMS WE WORK WITH</h2>
  <div class="cms-grid">
    <div class="cms-cell" style="color:#e0642a"><span class="cms-dot" style="background:#e0642a"></span>Marrowcart</div>
    <div class="cms-cell" style="color:#111"><span class="cms-dot" style="background:#111"></span>Plix</div>
    <div class="cms-cell" style="color:#c4201c">Tracks</div>
    <div class="cms-cell" style="color:#222;font-size:15px">BOXFIELD</div>
    <div class="cms-cell" style="color:#2e4a7a">Jumblo</div>
    <div class="cms-cell" style="color:#3a6f96"><span class="cms-dot" style="background:#3a6f96"></span>Inkpress</div>
    <div class="cms-cell" style="color:#6b9a1f">needstore</div>
    <div class="cms-cell" style="color:#d6262f"><span class="cms-dot" style="background:#d6262f"></span>Vertexa</div>
    <div class="cms-cell" style="color:#1f2a1a">Shelvio</div>
    <div class="cms-cell" style="color:#333;font-size:16px">placecore</div>
    <div class="cms-cell" style="color:#333"><span class="cms-dot" style="background:#333"></span>wraith</div>
    <div class="cms-cell" style="color:#4353ff"><span class="cms-dot" style="background:#4353ff"></span>Weavely</div>
    <div class="cms-cell" style="color:#1f7ac0">Droplet</div>
    <div class="cms-cell" style="color:#3a9fd6">Reflux</div>
    <div class="cms-cell" style="color:#8ab33c">banjo CMS</div>
    <div class="cms-cell" style="color:#6e9e2a">Marigolda</div>
  </div>
</section>

<!-- Thank you -->
<section class="slide slide--thanks">
  <div class="thanks-bg" role="img" aria-label="Dark blue abstract background of glowing network connections"></div>
  <h2 class="thanks-title">THANK YOU</h2>
  <div class="abs brand thanks-brand"><span class="brand__box"></span>FenLoopVault</div>
  <h3 class="abs contact-title">CONTACT<br>INFORMATION</h3>
  <div class="contact-row" style="top:257px">
    <span class="contact-row__icon"><svg width="20" height="20" viewBox="0 0 24 24" aria-hidden="true"><path fill="#fff" d="M6.6 10.8a15.2 15.2 0 006.6 6.6l2.2-2.2a1 1 0 011-.25 11.4 11.4 0 003.6.57 1 1 0 011 1V20a1 1 0 01-1 1A17 17 0 013 4a1 1 0 011-1h3.5a1 1 0 011 1c0 1.25.2 2.45.57 3.57a1 1 0 01-.25 1z"/></svg></span>
    +44 7700 900418
  </div>
  <div class="contact-rule" style="top:325px"></div>
  <div class="contact-row" style="top:350px">
    <span class="contact-row__icon"><svg width="22" height="22" viewBox="0 0 24 24" aria-hidden="true" fill="none" stroke="#fff" stroke-width="1.8"><circle cx="12" cy="12" r="9"/><ellipse cx="12" cy="12" rx="4" ry="9"/><line x1="3" y1="12" x2="21" y2="12"/></svg></span>
    Fenloopvault.com
  </div>
  <div class="contact-rule" style="top:418px"></div>
  <div class="contact-row" style="top:446px">
    <span class="contact-row__icon"><svg width="20" height="20" viewBox="0 0 24 24" aria-hidden="true"><rect x="3" y="5" width="18" height="14" rx="2" fill="#fff"/><polyline points="3,7 12,13 21,7" fill="none" stroke="#c8337d" stroke-width="1.8"/></svg></span>
    contact@fenloopvault.com
  </div>
</section>

</body>
</html>
```